Personal Biography Website for a Professional Game Developer

I'm looking for someone to design a personal biography website for a professional game developer. Look at the attached logos, headshots, and art as examples of the type of style that I'm looking for. This should be an edgy, progressive-style website -- like one you'd expect from a video game website.
I'm also a huge fan of the velmo website... large images for each section with little text.
I've attached the bio text as well (the underlines are just place holders)
Target Market(s)
Venture Capital, Video Game Developers
Number of Pages Required
1 page
Look and feel
Each slider illustrates characteristics of the customer's brand and the style your logo design should communicate.

```html
<!DOCTYPE html>
<html lang="en">
<head>
<meta charset="utf-8">
<title>Arden V7 — Professional Game Developer</title>
<link rel="stylesheet" href="https://fonts.googleapis.com/css2?family=Oswald:wght@300;400;600;700&family=Poppins:wght@400;500;600&family=Russo+One&display=swap">
<style>
:root{
  --red:#e31e24;
  --blue:#0a9be0;
  --hero:#0c0d15;
  --navy:#1c1b2b;
  --deep:#13131f;
  --card:#222233;
  --white:#ffffff;
  --ink:#1b1b22;
  --muted:#5a5a66;
  --footer:#0e0e1b;
}
*{margin:0;padding:0;box-sizing:border-box}
html,body{width:1200px;height:3780px;overflow:hidden}
body{position:relative;background:var(--navy);font-family:'Poppins',sans-serif;color:var(--white)}
.layer{position:absolute;left:0;top:0;width:1200px;height:3780px}
.abs{position:absolute}
.btn{position:absolute;background:var(--red);color:#fff;font:600 14px 'Poppins',sans-serif;border-radius:24px;display:flex;align-items:center;justify-content:center;white-space:nowrap}
.photo{position:absolute;border:1px solid rgba(255,255,255,.12)}
/* header */
.follow{left:172px;top:14px;font-size:13px;font-weight:500;display:flex;align-items:center;gap:8px}
.dot{width:17px;height:17px;border-radius:50%;background:#fff;display:inline-block}
.nav{top:76px;font-size:14px;font-weight:500;display:flex;gap:40px}
.nav a{color:#fff;text-decoration:none}
.nav .active{border-bottom:3px solid var(--red);padding-bottom:6px}
.brand{left:540px;top:66px;width:120px;text-align:center;font:700 30px/1 'Oswald',sans-serif;color:var(--red)}
.navline{top:52px;height:1px;width:330px;background:linear-gradient(90deg,transparent,rgba(255,255,255,.35),transparent)}
/* hero */
.pro{left:172px;top:226px;font:600 40px 'Oswald',sans-serif}
.gamedev{left:172px;top:280px;font:400 84px/1.1 'Russo One',sans-serif;color:var(--blue);font-style:italic}
/* headings */
.h2{font-family:'Oswald',sans-serif;font-size:58px;text-align:center;width:1200px;left:0}
.h2 .thin{font-weight:300;color:var(--blue)}
.h2 .bold{font-weight:700}
/* about */
.about1{left:247px;top:840px;font:300 66px 'Oswald',sans-serif;color:var(--blue)}
.about2{left:170px;top:910px;font:700 68px 'Oswald',sans-serif;letter-spacing:10px}
.aboutp{left:172px;top:1008px;width:370px;font-size:16px;line-height:30px}
/* dev cards */
.dev{position:absolute;top:1573px;width:268px;height:400px;background:var(--card);border-radius:28px;overflow:hidden}
.dev .img{height:286px;border-radius:28px}
.dev h3{font:500 17px 'Poppins',sans-serif;margin:18px 0 0 20px}
.pill{position:absolute;left:14px;top:337px;width:160px;height:40px;border:2px solid var(--red);border-radius:22px}
.pill span{position:absolute;left:0;top:0;height:36px;width:106px;background:var(--red);border-radius:20px;font:600 13px/36px 'Poppins',sans-serif;text-align:center}
.pill svg{position:absolute;right:18px;top:10px}
.circ{position:absolute;width:54px;height:54px;border-radius:50%;display:flex;align-items:center;justify-content:center}
/* blog */
.post{position:absolute;top:2325px;width:268px;height:420px;background:#fff;border-radius:14px;box-shadow:0 4px 18px rgba(0,0,0,.12);overflow:hidden;color:var(--ink)}
.post .img{height:210px;border-radius:14px 14px 0 0}
.date{position:absolute;left:18px;top:238px;background:var(--blue);color:#fff;font:600 10px 'Poppins',sans-serif;padding:3px 12px;border-radius:10px}
.post h4{position:absolute;left:16px;top:258px;font:500 17px 'Poppins',sans-serif}
.post p{position:absolute;left:16px;top:288px;width:236px;font-size:13.5px;line-height:20px;color:var(--muted)}
.post .btn{left:18px;top:362px;width:128px;height:36px;font-size:13px}
/* contact */
.field{position:absolute;background:#fff;color:#666;font-size:14px;padding:8px 10px}
/* footer */
.fh{font:600 13px 'Oswald',sans-serif;letter-spacing:.5px}
.links{list-style:none;font-size:13.5px;line-height:28.5px}
.links li::before{content:"";display:inline-block;width:12px;height:2px;background:var(--red);vertical-align:middle;margin-right:6px}
.info{font-size:13.5px;line-height:26px}
.copy{left:700px;top:3678px;width:328px;font-size:13px;text-align:right;white-space:nowrap}
</style>
</head>
<body>

<svg class="layer" viewBox="0 0 1200 3780" aria-hidden="true">
  <defs>
    <linearGradient id="contactBg" x1="0" y1="0" x2="0" y2="1">
      <stop offset="0" stop-color="#1a1a38"/><stop offset="1" stop-color="#0f0f22"/>
    </linearGradient>
  </defs>
  <rect width="1200" height="3780" fill="var(--navy)"/>
  <path d="M0,0 H1200 V495 C950,640 700,735 450,730 C250,725 100,690 0,640 Z" fill="var(--hero)"/>
  <rect x="0" y="2080" width="1200" height="800" fill="#fff"/>
  <path d="M0,1560 C250,1390 500,1310 700,1313 C900,1318 1080,1370 1200,1420 V1950 C1000,2080 700,2190 450,2190 C250,2190 100,2140 0,2090 Z" fill="var(--deep)"/>
  <path d="M0,1540 C250,1365 500,1285 700,1290 C900,1295 1080,1345 1200,1395 V1420 C1080,1370 900,1318 700,1313 C500,1310 250,1390 0,1560 Z" fill="var(--red)"/>
  <path d="M0,2090 C100,2140 250,2190 450,2190 C700,2190 1000,2080 1200,1950 V1968 C1000,2100 700,2210 450,2210 C250,2210 100,2160 0,2112 Z" fill="var(--red)"/>
  <path d="M0,3050 C200,2910 400,2822 600,2812 C850,2808 1050,2845 1200,2890 V3780 H0 Z" fill="url(#contactBg)"/>
  <path d="M0,3030 C200,2890 400,2800 600,2790 C850,2785 1050,2820 1200,2865 V2890 C1050,2845 850,2808 600,2812 C400,2822 200,2910 0,3050 Z" fill="var(--red)"/>
  <path d="M0,3322 C200,3392 400,3428 620,3428 C850,3428 1050,3400 1200,3365 V3780 H0 Z" fill="var(--footer)"/>
  <path d="M0,3300 C200,3370 400,3405 620,3405 C850,3405 1050,3380 1200,3345 V3365 C1050,3400 850,3428 620,3428 C400,3428 200,3392 0,3322 Z" fill="var(--red)"/>
</svg>

<!-- HEADER -->
<div class="abs follow">Follow us: <i class="dot"></i><i class="dot"></i><i class="dot"></i><i class="dot"></i></div>
<div class="btn" style="left:910px;top:11px;width:118px;height:32px;font-size:13px">Get In Touch</div>
<div class="abs navline" style="left:172px"></div>
<div class="abs navline" style="left:690px"></div>
<nav class="abs nav" style="left:182px"><a class="active">Home</a><a>About Me</a><a>Activity</a><a>Sponsor</a></nav>
<div class="abs brand">ARDEN V7</div>
<nav class="abs nav" style="left:687px"><a>Blog</a><a>Game</a><a>Players</a><a>Contact</a></nav>

<!-- HERO -->
<div class="photo" role="img" aria-label="Portrait of the game developer lit in red and blue neon" style="left:640px;top:135px;width:330px;height:545px;background:linear-gradient(160deg,#2a5fa0 0%,#163763 45%,#0e1a33 80%,#3a1420 100%)"></div>
<svg class="abs" style="left:80px;top:300px" width="30" height="46" aria-hidden="true"><path d="M24,2 L4,23 L24,44" fill="none" stroke="#fff" stroke-width="2"/></svg>
<svg class="abs" style="left:1090px;top:300px" width="30" height="46" aria-hidden="true"><path d="M6,2 L26,23 L6,44" fill="none" stroke="#fff" stroke-width="2"/></svg>
<div class="abs pro">PROFESSIONAL</div>
<div class="abs gamedev">Game<br>Developer</div>
<div class="btn" style="left:172px;top:496px;width:160px;height:44px">Know More</div>

<!-- ABOUT -->
<div class="photo" role="img" aria-label="Black and white portrait of the game developer with signature below" style="left:640px;top:770px;width:360px;height:510px;background:linear-gradient(170deg,#8a8a92 0%,#55555f 50%,#2a2a38 100%)"></div>
<div class="abs" style="left:172px;top:848px;width:62px;height:62px;border-radius:50%;background:var(--red)"></div>
<div class="abs about1">ABOUT</div>
<div class="abs about2">MYSELF</div>
<p class="abs aboutp">Establishing my services on a foundation of integrity, I am a highly dynamic Engineering Executive who has been passionately accentuating the gaming/entertainment experience for the last 10+ years.</p>
<div class="btn" style="left:172px;top:1185px;width:204px;height:44px;font-size:13px">Learn More About Me</div>

<!-- LATEST DEVELOPMENT -->
<h2 class="abs h2" style="top:1455px"><span class="thin">LATEST</span> <span class="bold">DEVELOPMENT</span></h2>

<div class="circ" style="left:103px;top:1710px;background:#23232f"><svg width="22" height="18" aria-hidden="true"><path d="M21,9 H2 M9,2 L2,9 L9,16" fill="none" stroke="#fff" stroke-width="2.4"/></svg></div>
<div class="circ" style="left:1049px;top:1710px;background:var(--blue)"><svg width="22" height="18" aria-hidden="true"><path d="M1,9 H20 M13,2 L20,9 L13,16" fill="none" stroke="#fff" stroke-width="2.4"/></svg></div>

<article class="dev" style="left:172px">
  <div class="img" role="img" aria-label="Game art: lone soldier silhouette against an orange sunset" style="background:linear-gradient(180deg,#e09354 0%,#b8612e 55%,#4a2414 100%)"></div>
  <h3>Iron Vigil</h3>
  <div class="pill"><span>Learn More</span><svg width="20" height="16" aria-hidden="true"><path d="M1,8 H18 M12,2 L18,8 L12,14" fill="none" stroke="#fff" stroke-width="2.2"/></svg></div>
</article>
<article class="dev" style="left:465px">
  <div class="img" role="img" aria-label="Game art: spaceship flying over colourful alien planets" style="background:linear-gradient(160deg,#4b2a9c 0%,#7b4fd6 45%,#e3588f 70%,#3a66c9 100%)"></div>
  <h3>Hollow Spire 2</h3>
  <div class="pill"><span>Learn More</span><svg width="20" height="16" aria-hidden="true"><path d="M1,8 H18 M12,2 L18,8 L12,14" fill="none" stroke="#fff" stroke-width="2.2"/></svg></div>
</article>
<article class="dev" style="left:757px">
  <div class="img" role="img" aria-label="Game art: giant sea serpent rising from stormy water" style="background:linear-gradient(170deg,#a5b3ad 0%,#5d7470 50%,#2b3a38 100%)"></div>
  <h3>Tunnel: Drift</h3>
  <div class="pill"><span>Learn More</span><svg width="20" height="16" aria-hidden="true"><path d="M1,8 H18 M12,2 L18,8 L12,14" fill="none" stroke="#fff" stroke-width="2.2"/></svg></div>
</article>

<!-- BLOG & NEWS -->
<h2 class="abs h2" style="top:2215px;color:var(--ink)"><span class="thin">BLOG &amp;</span> <span class="bold">NEWS</span></h2>
<div class="circ" style="left:103px;top:2499px;background:#fff;box-shadow:0 3px 12px rgba(0,0,0,.15)"><svg width="22" height="18" aria-hidden="true"><path d="M21,9 H2 M9,2 L2,9 L9,16" fill="none" stroke="#111" stroke-width="2.4"/></svg></div>
<div class="circ" style="left:1049px;top:2499px;background:#fff;box-shadow:0 3px 12px rgba(0,0,0,.15)"><svg width="22" height="18" aria-hidden="true"><path d="M1,9 H20 M13,2 L20,9 L13,16" fill="none" stroke="var(--blue)" stroke-width="2.4"/></svg></div>

<article class="post" style="left:172px">
  <div class="img" role="img" aria-label="Photo: hands typing code on a laptop in neon light" style="background:linear-gradient(135deg,#2a1a4a,#8a2f8f 55%,#2d5bd6)"></div>
  <span class="date">Feb 16, 2022</span>
  <h4>Nullam hendrerit urna</h4>
  <p>Lorem ipsum dolor sittetur adipiscing elit. Integer sit amet eleifend mauris.</p>
  <div class="btn">Learn More</div>
</article>
<article class="post" style="left:465px">
  <div class="img" role="img" aria-label="Photo: gamer playing a first-person game at a desk" style="background:linear-gradient(135deg,#5a4a2a,#2a2a2f 55%,#151518)"></div>
  <span class="date">Feb 16, 2022</span>
  <h4>Nullam hendrerit urna</h4>
  <p>Lorem ipsum dolor sittetur adipiscing elit. Integer sit amet eleifend mauris.</p>
  <div class="btn">Learn More</div>
</article>
<article class="post" style="left:759px">
  <div class="img" role="img" aria-label="Photo: designer drawing on a graphics tablet" style="background:linear-gradient(135deg,#1b6fb0,#2b93d6 50%,#0d3f6a)"></div>
  <span class="date">Feb 16, 2022</span>
  <h4>Nullam hendrerit urna</h4>
  <p>Lorem ipsum dolor sittetur adipiscing elit. Integer sit amet eleifend mauris.</p>
  <div class="btn">Learn More</div>
</article>

<!-- GET IN TOUCH -->
<h2 class="abs h2" style="top:2932px"><span class="thin">GET IN</span> <span class="bold">TOUCH</span></h2>
<div class="field" style="left:235px;top:3034px;width:237px;height:35px">Name</div>
<div class="field" style="left:481px;top:3034px;width:238px;height:35px">Email</div>
<div class="field" style="left:728px;top:3034px;width:237px;height:35px">Phone</div>
<div class="field" style="left:235px;top:3081px;width:730px;height:115px">Message</div>
<div class="btn" style="left:535px;top:3223px;width:130px;height:38px;font-size:13px">Send Now</div>

<!-- FOOTER -->
<div class="abs" style="left:172px;top:3560px;font:700 40px 'Oswald',sans-serif;color:var(--red)">ARDEN V7</div>
<div class="abs fh" style="left:387px;top:3476px">QUICK LINKS</div>
<ul class="abs links" style="left:387px;top:3506px"><li>Home</li><li>About Me</li><li>Activity</li><li>Sponsor</li><li>Blog</li><li>Game</li><li>Players</li><li>Contact</li></ul>
<div class="abs fh" style="left:575px;top:3476px">CONTACT INFO</div>
<div class="abs info" style="left:575px;top:3508px">
  <div style="display:flex;gap:10px"><svg width="12" height="16" aria-hidden="true" style="margin-top:5px"><path d="M6,15 C2,9 1,7 1,5.5 A5,5 0 0 1 11,5.5 C11,7 10,9 6,15 Z" fill="var(--blue)"/><circle cx="6" cy="5.5" r="1.8" fill="#0e0e1b"/></svg><span>48 Ember Lane, 9 Avenue,<br>Northvale, NV 40210-1100</span></div>
  <div style="display:flex;gap:10px;margin-top:8px"><svg width="14" height="14" aria-hidden="true" style="margin-top:6px"><path d="M3,1 L6,1 L7,4.5 L5,6 C6,8 8,9.5 9,10 L10.5,8 L14,9 L14,12 C14,13 13,14 12,14 C6,14 1,8 1,3 C1,2 2,1 3,1 Z" fill="var(--blue)"/></svg><span>01 555 010 247</span></div>
  <div style="display:flex;gap:10px;margin-top:8px"><svg width="14" height="11" aria-hidden="true" style="margin-top:8px"><rect width="14" height="11" rx="1" fill="var(--blue)"/><path d="M1,1 L7,6 L13,1" fill="none" stroke="#0e0e1b" stroke-width="1.3"/></svg><span>hello@ardenv7.com</span></div>
</div>
<div class="abs fh" style="left:575px;top:3660px">STAY CONNECTED</div>
<div class="abs" style="left:575px;top:3694px;display:flex;gap:11px"><i class="dot" style="width:26px;height:26px"></i><i class="dot" style="width:26px;height:26px"></i><i class="dot" style="width:26px;height:26px"></i><i class="dot" style="width:26px;height:26px"></i></div>
<div class="abs" style="left:843px;top:3530px;font:700 44px 'Oswald',sans-serif;color:var(--blue)">ARDEN V7</div>
<div class="abs copy">© 2022 <span style="color:var(--blue)">Arden V7</span> All right reserved</div>

</body>
</html>
```